SKVC Stationary and business Card
SKVC letterhead and Business Card
Professional
Summit Kinship Vitality Center
Dr. Marcus Pellham, D.C. Dr. Tamsin Pellham, D.C.
2948 Arden Avenue Boulder, CO 80304
drpellham@summitvitalityclinics.com
www.summitvitalityclinics.com

```html
<!DOCTYPE html>
<html lang="en">
<head>
<meta charset="utf-8">
<title>SKVC Business Card Concepts</title>
<link href="https://fonts.googleapis.com/css2?family=Cinzel:wght@400;600&family=Cormorant+SC:wght@500&display=swap" rel="stylesheet">
<style>
  :root {
    --stage: #ece6dc;
    --purple: #7a4b9c;
    --purple-dark: #633a84;
    --purple-light: #9a6bbb;
    --white: #ffffff;
    --ink: #5b4a66;
    --label: #3a3340;
  }
  * { box-sizing: border-box; margin: 0; padding: 0; }
  html, body { width: 1200px; height: 794px; overflow: hidden; }
  body {
    background: var(--stage);
    position: relative;
    font-family: "Cormorant SC", serif;
  }
  .card {
    position: absolute;
    width: 540px;
    height: 300px;
    border-radius: 16px;
    overflow: hidden;
    box-shadow: 0 2px 6px rgba(0,0,0,0.18);
  }
  .card--white { background: var(--white); color: var(--ink); }
  .card--purple {
    background: radial-gradient(ellipse at 50% 40%, var(--purple-light), var(--purple) 60%, var(--purple-dark));
    color: var(--white);
  }
  .front-a { left: 30px; top: 40px; }
  .front-b { left: 632px; top: 40px; }
  .back-a { left: 30px; top: 440px; }
  .back-b { left: 632px; top: 440px; }

  .card__wave { position: absolute; left: 0; bottom: 0; width: 540px; height: 300px; }

  .brand {
    position: absolute;
    top: 38px; left: 0; width: 100%;
    text-align: center;
    font-family: "Cinzel", serif;
    font-weight: 400;
    line-height: 1;
  }
  .brand__name { display: block; font-size: 38px; letter-spacing: 0.5px; }
  .brand__sub { display: block; font-size: 19px; letter-spacing: 5px; margin-top: 4px; }
  .card--white .brand { color: var(--purple); }
  .card--purple .brand { color: var(--white); }

  .doctors {
    position: absolute;
    top: 146px; right: 286px;
    text-align: right;
    font-size: 11px;
    line-height: 1.5;
    letter-spacing: 0.4px;
    white-space: nowrap;
  }
  .address {
    position: absolute;
    top: 210px; right: 286px;
    text-align: right;
    font-size: 10.5px;
    letter-spacing: 0.3px;
    white-space: nowrap;
  }
  .contacts {
    position: absolute;
    top: 138px; left: 272px;
    list-style: none;
    font-size: 10px;
    line-height: 1;
    letter-spacing: 0.3px;
    white-space: nowrap;
  }
  .contacts li { display: flex; align-items: center; height: 20px; gap: 7px; }
  .contacts svg { width: 11px; height: 11px; flex: none; }
  .card--white .contacts svg { color: var(--purple); }
  .card--purple .contacts svg { color: var(--white); }

  .back-mark {
    position: absolute;
    left: 248px; top: 104px;
    width: 44px; height: 44px;
    border-radius: 50%;
  }
  .card--white .back-mark { background: var(--purple); }
  .card--purple .back-mark { background: var(--white); }
  .back-url {
    position: absolute;
    bottom: 24px; left: 0; width: 100%;
    text-align: center;
    font-size: 10px;
    letter-spacing: 3px;
  }
  .card--white .back-url { color: #8c8494; }

  .label {
    position: absolute;
    width: 540px;
    text-align: center;
    font-family: "Cinzel", serif;
    font-weight: 600;
    font-size: 20px;
    letter-spacing: 2px;
    color: var(--label);
  }
  .label--front { top: 402px; }
  .label--back { top: 756px; }
  .label--a { left: 30px; }
  .label--b { left: 632px; }
</style>
</head>
<body>

  <section class="card card--white front-a">
    <svg class="card__wave" viewBox="0 0 540 300" aria-hidden="true">
      <path d="M0 248 C160 205 360 268 540 212 L540 300 L0 300 Z" fill="var(--purple)"/>
      <path d="M0 276 C170 240 370 292 540 242" fill="none" stroke="var(--white)" stroke-width="3"/>
    </svg>
    <h1 class="brand"><span class="brand__name">SUMMIT KINSHIP</span><span class="brand__sub">VITALITY CENTER</span></h1>
    <p class="doctors">Dr. Marcus Pellham, D.C.<br>Dr. Tamsin Pellham, D.C.</p>
    <p class="address">2948 Arden Avenue Boulder, CO 80304</p>
    <ul class="contacts">
      <li><svg viewBox="0 0 12 12"><path d="M3 1 L5 3.5 L4 5 Q5 7 7 8 L8.5 7 L11 9 L9.5 11 Q4 10.5 1 2.5 Z" fill="currentColor"/></svg>303.555.0142</li>
      <li><svg viewBox="0 0 12 12"><rect x="1" y="4" width="10" height="5" rx="1" fill="currentColor"/><rect x="3" y="1" width="6" height="3" fill="currentColor"/><rect x="3" y="8" width="6" height="3" fill="currentColor"/></svg>303.555.0187</li>
      <li><svg viewBox="0 0 12 12"><rect x="1" y="2.5" width="10" height="7" rx="1" fill="currentColor"/><path d="M1.5 3 L6 7 L10.5 3" stroke="#fff" fill="none"/></svg>drpellham@summitvitalityclinics.com</li>
      <li><svg viewBox="0 0 12 12"><circle cx="6" cy="6" r="5" fill="none" stroke="currentColor"/><path d="M1 6 H11 M6 1 Q3 6 6 11 Q9 6 6 1" fill="none" stroke="currentColor"/></svg>www.summitvitalityclinics.com</li>
    </ul>
  </section>

  <section class="card card--purple front-b">
    <svg class="card__wave" viewBox="0 0 540 300" aria-hidden="true">
      <path d="M0 262 C170 220 360 280 540 226 L540 300 L0 300 Z" fill="var(--white)"/>
      <path d="M0 246 C170 206 370 262 540 210" fill="none" stroke="var(--white)" stroke-width="2" opacity="0.7"/>
    </svg>
    <h1 class="brand"><span class="brand__name">SUMMIT KINSHIP</span><span class="brand__sub">VITALITY CENTER</span></h1>
    <p class="doctors">Dr. Marcus Pellham, D.C.<br>Dr. Tamsin Pellham, D.C.</p>
    <p class="address">2948 Arden Avenue Boulder, CO 80304</p>
    <ul class="contacts">
      <li><svg viewBox="0 0 12 12"><path d="M3 1 L5 3.5 L4 5 Q5 7 7 8 L8.5 7 L11 9 L9.5 11 Q4 10.5 1 2.5 Z" fill="currentColor"/></svg>303.555.0142</li>
      <li><svg viewBox="0 0 12 12"><rect x="1" y="4" width="10" height="5" rx="1" fill="currentColor"/><rect x="3" y="1" width="6" height="3" fill="currentColor"/><rect x="3" y="8" width="6" height="3" fill="currentColor"/></svg>303.555.0187</li>
      <li><svg viewBox="0 0 12 12"><rect x="1" y="2.5" width="10" height="7" rx="1" fill="currentColor"/><path d="M1.5 3 L6 7 L10.5 3" stroke="var(--purple)" fill="none"/></svg>drpellham@summitvitalityclinics.com</li>
      <li><svg viewBox="0 0 12 12"><circle cx="6" cy="6" r="5" fill="none" stroke="currentColor"/><path d="M1 6 H11 M6 1 Q3 6 6 11 Q9 6 6 1" fill="none" stroke="currentColor"/></svg>www.summitvitalityclinics.com</li>
    </ul>
  </section>

  <p class="label label--front label--a">Business Card Front A</p>
  <p class="label label--front label--b">Business Card Front B</p>

  <section class="card card--white back-a">
    <div class="back-mark"></div>
    <p class="back-url">WWW.SUMMITVITALITYCLINICS.COM</p>
  </section>

  <section class="card card--purple back-b">
    <div class="back-mark"></div>
    <p class="back-url">WWW.SUMMITVITALITYCLINICS.COM</p>
  </section>

  <p class="label label--back label--a">Business Card Back A</p>
  <p class="label label--back label--b">Business Card Back B</p>

</body>
</html>
```